Business Cards Design for the electrical wholesaler: clean bold dynamic :)

We need a business card design that would follow our latest brand guidelines. As an electrical wholesaler we want to bring a fresh look and feel into the industry. The design should be clean bold and dynamic. It should come alive with the renewed energy of our green colour. Our grey colour should keep things balanced and complement the notion of maturity and responsibility. We employ Lato as a corporate font however are not bound by this font and we’re open to interpretation here.

Target Market(s)

Electrical contractors

Industry/Entity Type

Business

Contact Information for Business Card

Logo
Name & Surname: Olena Dovbush
Job Title: Director of Marketing
Email: helen.dovbush@mailvane.example
Cell phone: XXX.XXX.XXXX
Address: 20917 - 87 Ave. Edmonton, AB, Canada. T6K 2R8
Business Phone: 780.555.0187
Website: www.qorvil.example

Font styles to use
Other font styles liked:
• Lato

Requirements
Must have
• Logo & website
Nice to have
• Brand elements - some of them you may find in the attached Brand Guidelines (e.g. three lines on the background signifying "W")

```html
<!DOCTYPE html>
<html lang="en">
<head>
<meta charset="utf-8">
<title>Qorvil Business Card</title>
<link rel="stylesheet" href="https://fonts.googleapis.com/css2?family=Lato:wght@400;700;900&display=swap">
<style>
  :root {
    --brand-green: #8cc43f;
    --brand-grey: #4f5153;
    --ink: #3a3b3d;
    --card-white: #ffffff;
    --backdrop: #e3e4e6;
  }
  * { box-sizing: border-box; margin: 0; padding: 0; }
  html, body { width: 1200px; height: 800px; overflow: hidden; }
  body {
    background: var(--backdrop);
    font-family: "Lato", Arial, sans-serif;
    color: var(--ink);
    position: relative;
  }
  .card {
    position: absolute;
    top: 250px;
    width: 525px;
    height: 300px;
    background: var(--card-white);
    overflow: hidden;
    box-shadow: 0 6px 18px rgba(0,0,0,0.12);
  }
  .card--front { left: 50px; }
  .card--back { left: 625px; }

  .front__panel {
    position: absolute;
    inset: 0;
    background: var(--brand-grey);
    clip-path: polygon(67% 0, 100% 0, 100% 100%, 47% 100%);
  }
  .front__identity { position: absolute; left: 34px; top: 30px; }
  .front__name {
    font-size: 27px;
    font-weight: 900;
    color: var(--brand-green);
    line-height: 1.05;
  }
  .front__title { font-size: 14px; color: var(--ink); margin-top: 3px; }

  .front__contacts {
    position: absolute;
    left: 34px;
    top: 128px;
    list-style: none;
    font-size: 13.5px;
    line-height: 1.32;
    color: var(--ink);
  }
  .front__contacts li { display: flex; align-items: flex-start; gap: 8px; }
  .front__contacts li.gap-top { margin-top: 8px; }
  .contact-icon { width: 11px; height: 11px; margin-top: 4px; flex: none; fill: var(--brand-green); }

  .wordmark {
    font-family: "Lato", Arial, sans-serif;
    font-weight: 900;
    letter-spacing: -1px;
    display: flex;
    align-items: center;
  }
  .wordmark__square { display: inline-block; background: var(--brand-green); }
  .front__wordmark {
    position: absolute;
    right: 36px;
    bottom: 78px;
    font-size: 64px;
    color: var(--card-white);
    gap: 12px;
  }
  .front__wordmark .wordmark__square { width: 22px; height: 22px; }

  .back__content {
    position: absolute;
    inset: 0;
    display: flex;
    flex-direction: column;
    align-items: center;
    justify-content: center;
    gap: 26px;
  }
  .back__wordmark { font-size: 56px; color: var(--brand-grey); gap: 12px; }
  .back__wordmark .wordmark__square { width: 20px; height: 20px; }
  .back__website {
    font-size: 13px;
    letter-spacing: 9px;
    color: var(--ink);
  }
</style>
</head>
<body>
  <section class="card card--front">
    <div class="front__panel"></div>
    <div class="front__identity">
      <h1 class="front__name">Olena Dovbush</h1>
      <p class="front__title">Director of Marketing</p>
    </div>
    <ul class="front__contacts">
      <li>
        <svg class="contact-icon" viewBox="0 0 12 12"><rect x="0" y="1" width="12" height="10" rx="1.5"/></svg>
        <span>780.555.0187</span>
      </li>
      <li>
        <svg class="contact-icon" viewBox="0 0 12 12"><rect x="2.5" y="0" width="7" height="12" rx="1.2" fill="none" stroke="#8cc43f" stroke-width="1.4"/></svg>
        <span>XXX.XXX.XXXX</span>
      </li>
      <li class="gap-top">
        <svg class="contact-icon" viewBox="0 0 12 12"><circle cx="6" cy="6" r="5" fill="none" stroke="#8cc43f" stroke-width="1.4"/><path d="M1 6h10M6 1c-2.5 3-2.5 7 0 10M6 1c2.5 3 2.5 7 0 10" fill="none" stroke="#8cc43f" stroke-width="1"/></svg>
        <span>www.qorvil.example</span>
      </li>
      <li>
        <svg class="contact-icon" viewBox="0 0 12 12"><rect x="0" y="2" width="12" height="8" rx="1"/><path d="M0.5 2.5 6 7l5.5-4.5" fill="none" stroke="#fff" stroke-width="1.1"/></svg>
        <span>helen.dovbush@mailvane.example</span>
      </li>
      <li class="gap-top">
        <svg class="contact-icon" viewBox="0 0 12 12"><path d="M6 0a4 4 0 0 0-4 4c0 3 4 8 4 8s4-5 4-8a4 4 0 0 0-4-4zm0 5.6A1.6 1.6 0 1 1 6 2.4a1.6 1.6 0 0 1 0 3.2z"/></svg>
        <span>20917 - 87 Ave. Edmonton<br>AB, Canada. T6K 2R8</span>
      </li>
    </ul>
    <div class="wordmark front__wordmark">
      <span class="wordmark__square"></span>
      <span>qorvil</span>
    </div>
  </section>

  <section class="card card--back">
    <div class="back__content">
      <div class="wordmark back__wordmark">
        <span class="wordmark__square"></span>
        <span>qorvil</span>
      </div>
      <p class="back__website">www.qorvil.example</p>
    </div>
  </section>
</body>
</html>
```